M25 Billboard Advert Required Please

I need an advert for a motorway Billboard on the M25 , the advert should show the following in big letters:
GUTTER CLEANING
DALRYNFLUES.COM and a small logo off to the side (Our logo is attached)

The printer has requested the following (Important please) the advert has to be
pdf file / 300 dpi/landscape orientation / scaled to a minimum 25% advert size ( this particular site is 22ft x 10ft so 25% of this please). Please also make sure that the artwork is embedded and outlined correctly if this is incorrect it will affect the printing of the banner.

Target Market(s)

General Public

Industry/Entity Type

Gutter Cleaning

Requirements
Should not have
• No Change to our Logo

```html
<!DOCTYPE html>
<html lang="en">
<head>
<meta charset="utf-8">
<title>Dalryn Flues – Gutter Cleaning Billboard</title>
<link rel="stylesheet" href="https://fonts.googleapis.com/css2?family=Open+Sans:wght@700&family=Oswald:wght@700&display=swap">
<style>
  :root {
    --backdrop: #5a5a5a;
    --ink: #000000;
    --paper: #ffffff;
    --signal-red: #b70f20;
  }
  * { margin: 0; padding: 0; box-sizing: border-box; }
  html, body {
    width: 1000px;
    height: 1200px;
    overflow: hidden;
    background: var(--backdrop);
  }
  .billboard {
    position: absolute;
    left: 30px;
    top: 365px;
    width: 940px;
    height: 470px;
    overflow: hidden;
    box-shadow: 0 10px 40px rgba(0,0,0,0.5);
  }
  .billboard-bands {
    position: absolute;
    inset: 0;
    width: 100%;
    height: 100%;
  }
  .brand {
    position: absolute;
    top: 62px;
    left: 0;
    width: 100%;
    display: flex;
    justify-content: center;
    align-items: center;
    gap: 18px;
  }
  .brand-mark {
    width: 40px;
    height: 40px;
    background: var(--signal-red);
  }
  .brand-name {
    font-family: "Open Sans", sans-serif;
    font-weight: 700;
    font-size: 54px;
    line-height: 1;
    color: var(--ink);
    letter-spacing: -0.01em;
  }
  .tagline {
    position: absolute;
    top: 160px;
    left: 0;
    width: 100%;
    text-align: center;
    font-family: "Open Sans", sans-serif;
    font-weight: 700;
    font-size: 26px;
    color: var(--ink);
  }
  .headline {
    position: absolute;
    top: 236px;
    left: 0;
    width: 100%;
    text-align: center;
    font-family: "Oswald", sans-serif;
    font-weight: 700;
    font-size: 96px;
    line-height: 1.1;
    color: var(--paper);
    text-transform: uppercase;
  }
  .web-address {
    position: absolute;
    top: 384px;
    left: 0;
    width: 100%;
    text-align: center;
    font-family: "Oswald", sans-serif;
    font-weight: 700;
    font-size: 50px;
    line-height: 1.2;
    letter-spacing: 0.09em;
    color: var(--paper);
  }
</style>
</head>
<body>
  <section class="billboard">
    <svg class="billboard-bands" viewBox="0 0 1458 728" preserveAspectRatio="none" aria-hidden="true">
      <rect width="1458" height="728" fill="var(--ink)"/>
      <polygon points="0,20 1458,20 1458,180 1255,548 200,548 0,200" fill="var(--signal-red)"/>
      <polygon points="0,0 1458,0 1458,20 1280,343 180,343 0,20" fill="var(--paper)"/>
    </svg>
    <div class="brand">
      <span class="brand-mark"></span>
      <span class="brand-name">Dalryn Flues</span>
    </div>
    <p class="tagline">Clean gutters protect your property</p>
    <h1 class="headline">Gutter Cleaning</h1>
    <p class="web-address">WWW.DALRYNFLUES.COM</p>
  </section>
</body>
</html>
```